Banner Ad Design Project

We are re-branding our energy management company called 'Voltaris'. We sell Energy Management Information Software and are currently positioned as a very technical organization. While we are always going to be very technical we want to shift away from telling people about the power of our software and become a more customer centric organization focusing on how energy management can solve many of your organizations problems. The final design should be modern and simple, as we are taking something very technical and complicated and trying to sell it. We need 4 banners created for our site www.voltaris-example.com which rotate across the top. They all need to be different and easily editable (preferably Photoshop)as we change marketing campaigns, the text needs to be editable.

The Size of the banners are 940 pixels by 250 pixels.
Updates

Thank you so much to everyone for you questions and for the few designs I have received. I am very new at this so please if there are things I can do to help better convey my design needs please let me know. Many people have asked for the Text to do on the banners. Here is what I have come up with for the 4 banners.

Banner 1

Maintain high building standards
                - With lower energy costs

Banner 2
Energy Reporting Requirements
                - Made effortless

Banner 3
Presenting Carl Benson, President of QELTRA, June 19th
- The future of Ontario’s power market

Banner 4
Working with utilities to develop and execute successful Energy Conservation Programs

As well we are working on re-branding ourselves so the website at this point does not convey the look and feel we are looking to go with. The attached files, especially the brochure and business card, convey the look and feel I am looking fore much better!

Reason: Need to check with the rest of my team to make final decision. Keep submitting designs, Thanks!

Industry/Entity Type

Marketing

Requirements
Must have
• The size needs to be 940 by 250 pixels. They need to contain the green color indicated in the 'Voltaris branding design features' document.

Needs to be consistent withe the look and feel of the brochure, PowerPoint and business card attached.

The integration of the 'Voltaris Head' and other similar graphics into the banners.
Should not have
• The look and feel of our current website

```html
<!DOCTYPE html>
<html lang="en">
<head>
<meta charset="utf-8">
<title>Banner – Maintain High Building Standards</title>
<link rel="stylesheet" href="https://fonts.googleapis.com/css2?family=Arvo&family=Carlito:wght@400;700&display=swap">
<style>
  :root {
    --stage: #212221;
    --brand-green: #80bd41;
    --forest: #1f5a2c;
    --icon-tone: #3d6b3a;
    --icon-light: #dcebcf;
    --white: #ffffff;
    --rule: #3b6b34;
  }
  * { margin: 0; padding: 0; box-sizing: border-box; }
  html, body {
    width: 1200px;
    height: 900px;
    overflow: hidden;
    background: var(--stage);
  }
  .banner {
    position: absolute;
    left: 36px;
    top: 300px;
    width: 1128px;
    height: 300px;
    background: var(--brand-green);
  }
  .banner__icon {
    position: absolute;
    left: 114px;
    top: 18px;
    width: 252px;
    height: 270px;
    border-radius: 6px;
    background: linear-gradient(160deg, var(--icon-tone) 0%, #5b8f45 55%, var(--icon-light) 100%);
  }
  .banner__headline {
    position: absolute;
    left: 466px;
    top: 36px;
    font-family: "Arvo", "Rockwell", serif;
    font-weight: 400;
    font-size: 57px;
    line-height: 72px;
    color: var(--white);
    letter-spacing: 0.3px;
    white-space: nowrap;
  }
  .banner__tagline {
    position: absolute;
    left: 466px;
    top: 204px;
    width: 416px;
    height: 51px;
    border-top: 1.5px dashed var(--rule);
    border-bottom: 1.5px dashed var(--rule);
    display: flex;
    align-items: center;
    padding-left: 15px;
    font-family: "Carlito", "Calibri", sans-serif;
    font-weight: 700;
    font-size: 26px;
    letter-spacing: 1.8px;
    color: var(--forest);
    text-transform: uppercase;
    white-space: nowrap;
  }
</style>
</head>
<body>
  <section class="banner" aria-label="Energy savings banner">
    <div class="banner__icon" role="img" aria-label="Icon of an office tower and factory with a dollar coin and downward arrow, representing lower energy costs"></div>
    <h1 class="banner__headline">Maintain High<br>Building Standards</h1>
    <p class="banner__tagline">With lower energy costs</p>
  </section>
</body>
</html>
```